New bag packaging for chewy candy

We need a new packaging for our fruit chewy candy range (7 flavours in all). The product will have to showcase our trademark and feature the fruit of the product's flavour. We require the packaging to have an equal look and adaptable to 7 flavours, to make it have the appearance that it is part of a range of products as opposed to a standalone. New design preferred. Please keep it playful but simple and yet stand out on an aisle shelf already full of colours. Dimensions of bag is 130mm (W) x 205mm (H). Allow for information on the back folds. Example of existing packaging given. Winner will get extra to adapt the packaging to the other 6 flavours.

Target Market(s)

Supermarket crowd

Industry/Entity Type

Product

Requirements
Must have
• Trademark, Flavour, picture of fruit lfavour
Nice to have
• Open to bold colours

```html
<!DOCTYPE html>
<html lang="en">
<head>
<meta charset="utf-8">
<title>Jolly Chews – Strawberry Chewy Candy Bag</title>
<link href="https://fonts.googleapis.com/css2?family=Cherry+Swash:wght@700&family=Roboto:wght@500;700;900&display=swap" rel="stylesheet">
<style>
  :root{
    --plum:#8c1a6c;
    --header-pink:#d9479a;
    --header-glow:#f6a8d2;
    --blush:#fbe9f3;
    --lavender:#c7a6d8;
    --lower-pink:#df6cb0;
    --ribbon:#8a3a97;
    --ribbon-dark:#5f2270;
    --title:#9a2f8a;
    --sun:#ffe22a;
    --berry:#d8283a;
    --candy:#ef8fd6;
    --white:#ffffff;
    --text-font:"Roboto", Arial, sans-serif;
    --title-font:"Cherry Swash", Georgia, serif;
  }
  *{margin:0;padding:0;box-sizing:border-box;}
  html,body{width:984px;height:1200px;overflow:hidden;background:var(--white);}
  .canvas{position:relative;width:984px;height:1200px;}
  .bag-shapes{position:absolute;inset:0;}
  .brand{
    position:absolute;left:143px;width:698px;top:256px;
    display:flex;align-items:center;justify-content:center;gap:16px;
  }
  .brand-dot{width:46px;height:46px;border-radius:50%;background:var(--sun);}
  .brand-name{
    font-family:var(--text-font);font-weight:900;font-size:70px;
    color:var(--sun);letter-spacing:1px;line-height:1;
  }
  .flavour{
    position:absolute;left:143px;width:698px;top:452px;text-align:center;
    font-family:var(--title-font);font-weight:700;font-size:112px;line-height:1;
    color:var(--title);letter-spacing:2px;
  }
  .product-art{
    position:absolute;left:300px;top:605px;width:355px;height:255px;
    border-radius:48px;
    background:linear-gradient(180deg,var(--berry) 0%,var(--berry) 48%,var(--candy) 100%);
  }
  .halal-seal{
    position:absolute;left:180px;top:895px;width:88px;height:88px;border-radius:50%;
    border:4px solid var(--white);
  }
  .product-type{
    position:absolute;left:290px;width:380px;top:918px;text-align:center;
    font-family:var(--text-font);font-weight:700;font-size:34px;color:var(--white);
    letter-spacing:1px;line-height:40px;
  }
  .tagline{
    position:absolute;left:330px;width:300px;top:975px;height:44px;
    display:flex;align-items:center;justify-content:center;
    font-family:var(--text-font);font-weight:700;font-size:26px;color:var(--white);letter-spacing:1px;
  }
  .vitamin-badge{
    position:absolute;left:650px;top:862px;width:138px;height:138px;border-radius:50%;
    background:var(--ribbon);border:6px solid var(--white);
    display:flex;flex-direction:column;align-items:center;justify-content:center;
    font-family:var(--text-font);color:var(--white);line-height:1;
  }
  .vitamin-badge .small{font-size:17px;font-weight:700;}
  .vitamin-badge .big{font-size:44px;font-weight:900;margin:4px 0;}
  .vitamin-badge .note{font-size:12px;font-weight:700;}
</style>
</head>
<body>
<main class="canvas">
  <svg class="bag-shapes" width="984" height="1200" viewBox="0 0 984 1200" aria-hidden="true">
    <defs>
      <radialGradient id="headerGlow" cx="0.5" cy="0.45" r="0.6">
        <stop offset="0" stop-color="var(--header-glow)"/>
        <stop offset="1" stop-color="var(--header-pink)"/>
      </radialGradient>
    </defs>
    <rect x="143" y="66" width="698" height="1071" fill="var(--blush)"/>
    <path d="M143 690 Q470 860 841 560 L841 1070 L143 1070 Z" fill="var(--lower-pink)"/>
    <path d="M143 655 Q470 820 841 520 L841 560 Q470 860 143 690 Z" fill="var(--lavender)"/>
    <path d="M143 388 Q500 360 841 314 L841 350 Q500 400 143 440 Z" fill="var(--lavender)"/>
    <path d="M143 156 L841 156 L841 300 Q500 350 143 376 Z" fill="url(#headerGlow)"/>
    <path d="M143 376 Q500 350 841 300" fill="none" stroke="var(--white)" stroke-width="8"/>
    <rect x="143" y="66" width="698" height="82" fill="var(--plum)"/>
    <rect x="143" y="148" width="698" height="8" fill="var(--white)"/>
    <rect x="143" y="1062" width="698" height="8" fill="var(--white)"/>
    <rect x="143" y="1070" width="698" height="67" fill="var(--plum)"/>
    <path d="M300 985 L342 985 L342 1025 L300 1025 L318 1005 Z" fill="var(--ribbon-dark)"/>
    <path d="M660 985 L618 985 L618 1025 L660 1025 L642 1005 Z" fill="var(--ribbon-dark)"/>
    <rect x="330" y="975" width="300" height="44" fill="var(--ribbon)"/>
  </svg>

  <div class="brand">
    <span class="brand-name">Jolly Chews</span>
    <span class="brand-dot"></span>
  </div>

  <div class="flavour">Strawberry</div>

  <div class="product-art" role="img" aria-label="Two ripe strawberries with four round pink chewy candies in front"></div>

  <div class="halal-seal" role="img" aria-label="Certification seal"></div>

  <div class="product-type">CHEWY CANDY</div>
  <div class="tagline">UNIQUE TASTE</div>

  <div class="vitamin-badge">
    <span class="small">contains</span>
    <span class="big">VIT.C</span>
    <span class="note">Conc. Apple Juice</span>
  </div>
</main>
</body>
</html>
```